Easy - Fix our "Win a Party" Promo Flyer

Please see attached promo flyer with all the information required. Looking for quick assistance so we can go live with the advertising for this competition. Looking for something more commercial and polished. Very attractive so that lots of people enter the competition. <br/><br/>Happy for it to look a little bit festive as the competition is running in December. <br/><br/>Attached is out Grill Kammer Logo and first attempts at poster. Please let me know if you need anything further. <br/><br/>If you see any grammar or spelling errors please feel free to fix too.
Corporate Businesses who are buying vouchers as staff christmas gifts/bonus

```html
<!DOCTYPE html>
<html lang="en">
<head>
<meta charset="utf-8">
<title>Grill Kammer – Win the Ultimate Staff Party</title>
<link href="https://fonts.googleapis.com/css2?family=Alfa+Slab+One&family=Rye&family=Oswald:wght@400;500&family=Montserrat:wght@400;600&display=swap" rel="stylesheet">
<style>
  :root{
    --bg:#e9e4dc;
    --red:#e3262b;
    --cream:#f6d98c;
    --white:#ffffff;
    --ink:#2b211d;
    --slate:#55504c;
    --glow-1:#fbe3b8;
    --glow-2:#d98a48;
    --glow-3:#6e3419;
    --glow-4:#2a140c;
  }
  *{margin:0;padding:0;box-sizing:border-box}
  html,body{width:1200px;height:960px;overflow:hidden;background:var(--bg)}
  .stage{position:relative;width:1200px;height:960px}
  .flyer{position:absolute;top:148px;width:450px;height:640px;overflow:hidden;box-shadow:6px 8px 18px rgba(0,0,0,.35)}
  .flyer--front{left:134px}
  .flyer--back{left:616px;background:var(--white)}
  .crowd-photo{position:absolute;inset:0;
    background:radial-gradient(ellipse at 70% 25%,var(--glow-1) 0%,var(--glow-2) 35%,var(--glow-3) 70%,var(--glow-4) 100%)}
  .abs{position:absolute;white-space:nowrap}
  .win{left:0;right:0;top:30px;text-align:center;font-family:"Rye",serif;font-size:108px;line-height:1;color:var(--red)}
  .win-sub{left:0;right:0;top:140px;text-align:center;font-family:"Alfa Slab One",serif;font-size:19px;color:var(--slate);letter-spacing:.5px}
  .for-you{left:43px;top:190px;font-family:"Oswald",sans-serif;font-size:29px;line-height:31px;color:var(--ink)}
  .for-you .accent{color:var(--red)}
  .offer{font-family:"Oswald",sans-serif;color:var(--white);line-height:1}
  .offer .cream{color:var(--cream)}
  .brand{font-family:"Oswald",sans-serif;font-weight:500;color:var(--red);text-align:center;line-height:1}
  .brand__dot{display:block;margin:0 auto 6px;width:20px;height:20px;border-radius:50%;background:var(--red)}
  .vouchers{left:340px;top:434px;width:68px}
  .vouchers span{display:block;height:22px;margin-bottom:6px;border-radius:2px}
  .xmas{left:318px;top:530px;width:110px;text-align:center;font-family:"Oswald",sans-serif;font-size:12.5px;line-height:15px;color:var(--ink)}

  .back-photo{position:absolute;inset:0;clip-path:polygon(412px 0,450px 0,450px 640px,220px 640px)}
  .back-body{font-family:"Montserrat",sans-serif;color:var(--ink)}
  .lead{left:37px;top:62px;font-size:15px;font-weight:600;line-height:19px}
  .lead .red{color:var(--red)}
  .includes-title{left:243px;top:134px;font-family:"Oswald",sans-serif;font-size:20px;color:var(--red)}
  .includes{left:35px;top:168px;width:310px;height:82px}
  .item{font-family:"Montserrat",sans-serif;font-weight:600;font-size:8.5px;color:var(--ink);text-align:center;line-height:10px}
  .more{left:33px;top:254px;font-size:11px;font-weight:600}
  .hurry{left:40px;top:284px;font-family:"Oswald",sans-serif;font-size:17px;line-height:24px;color:var(--red)}
  .hurry .two{display:inline-block;font-size:46px;line-height:24px;color:var(--ink);margin:0 4px}
  .cake{left:37px;top:328px;font-size:15.5px;font-weight:600;line-height:20px}
  .note{left:36px;font-size:11.5px;line-height:14.5px}
  .phone{left:34px;top:529px;font-family:"Oswald",sans-serif;font-weight:500;font-size:33px;color:var(--ink)}
  .email{left:34px;top:572px;font-family:"Oswald",sans-serif;font-size:16px;color:var(--ink)}
  .social{left:34px;top:594px;font-family:"Oswald",sans-serif;font-size:16px;color:var(--ink);display:flex;align-items:center;gap:6px}
  .social i{display:inline-block;width:18px;height:18px;border-radius:50%;background:#3b5ba8}
</style>
</head>
<body>
<main class="stage">

  <section class="flyer flyer--front">
    <div class="crowd-photo" role="img" aria-label="Concert crowd silhouette with a woman raising her fist against warm stage lights"></div>
    <h1 class="abs win">WIN</h1>
    <p class="abs win-sub">THE ULTIMATE STAFF PARTY</p>
    <p class="abs for-you"><span class="accent">For</span> You<br><span class="accent">&amp;</span> Your<br>Colleague</p>

    <div class="offer">
      <span class="abs cream" style="left:133px;top:354px;font-size:22px">Purchase</span>
      <span class="abs cream" style="left:124px;top:376px;font-size:42px">K5000</span>
      <span class="abs" style="left:118px;top:416px;font-size:18px">worth of vouchers</span>
      <span class="abs" style="left:114px;top:435px;font-size:25px">before</span>
      <span class="abs cream" style="left:109px;top:461px;font-size:26px">December</span>
      <span class="abs cream" style="left:212px;top:428px;font-size:64px">31<span style="font-size:20px">st</span></span>
      <span class="abs" style="left:110px;top:490px;font-size:25px">&amp; Go into the Draw</span>
      <span class="abs" style="left:110px;top:517px;font-size:25px">to Win the Ultimate</span>
      <span class="abs cream" style="left:110px;top:546px;font-size:42px">STAFF PARTY</span>
      <span class="abs" style="left:114px;top:590px;font-size:23px">for 150 people</span>
    </div>

    <div class="abs brand" style="left:316px;top:318px;width:104px">
      <span class="brand__dot"></span>
      <span style="font-size:30px">GRILL</span><br><span style="font-size:24px">KAMMER</span>
    </div>
    <div class="abs vouchers" role="img" aria-label="Sample shopping vouchers">
      <span style="background:#b89a62"></span>
      <span style="background:#f2c230"></span>
      <span style="background:#d9333a"></span>
    </div>
    <p class="abs xmas">Have a<br>Meaty Xmas<br>@Grill Kammer Crew</p>
  </section>

  <section class="flyer flyer--back back-body">
    <div class="back-photo crowd-photo" role="img" aria-label="Concert crowd silhouette with a raised hand against warm stage lights"></div>
    <p class="abs lead">Purchase <span class="red">K5000</span> worth of vouchers<br>before December 31st and go into the draw<br>to win the Ultimate STAFF PARTY<br>for 150 people.</p>
    <p class="abs includes-title">This Includes:</p>
    <svg class="abs includes" viewBox="0 0 310 82" aria-hidden="true">
      <g stroke="#1a1a1a" stroke-width="1.3">
        <line x1="30" y1="0" x2="10" y2="80"/>
        <line x1="100" y1="0" x2="80" y2="80"/>
        <line x1="170" y1="0" x2="150" y2="80"/>
        <line x1="240" y1="0" x2="220" y2="80"/>
        <line x1="310" y1="0" x2="290" y2="80"/>
      </g>
    </svg>
    <span class="abs item" style="left:66px;top:200px">A Venue</span>
    <span class="abs item" style="left:132px;top:195px">BBQ Style<br>PNG Menu</span>
    <span class="abs item" style="left:208px;top:200px">Roast Pig</span>
    <span class="abs item" style="left:284px;top:200px">Decor</span>
    <p class="abs more">&amp; Much More...</p>
    <p class="abs hurry">So Hurry! There are Only<span class="two">2</span>Parties to Win</p>
    <p class="abs cake">Will Even Throw in an Extra<br>Large Themed Cake with Your<br>Company Logo in it.</p>
    <p class="abs note" style="top:401px">Tip: Buy More Vouchers to Have<br>Better Chances of Winning</p>
    <p class="abs note" style="top:443px">For Every HR Department Enquiry<br>We Receive, A Special Surprise<br>will be given.</p>
    <p class="abs note" style="top:497px">So Hurry Up! And Contact us<br>Below on</p>
    <p class="abs phone">4810 3375</p>
    <p class="abs email">sales@grillkammer-events.com</p>
    <p class="abs social"><i></i>grillkammerhq</p>
    <div class="abs brand" style="left:330px;top:490px;width:96px">
      <span class="brand__dot"></span>
      <span style="font-size:30px">GRILL</span><br><span style="font-size:23px">KAMMER</span>
    </div>
  </section>

</main>
</body>
</html>
```